Meridale Dental Business Card

Please design a professional but colorful looking business card. Our new logo is attached. The card also needs the following information:
For ALL Your Dental Needs
Curtis L. Hobbel, D.D.S.
918-555-0147
20463-C North Fernwick, Bixby, OK 74031
www.meridaledentalok.example

Industry/Entity Type

Business

Colors

Designer to choose colors to be used in the design.

```html
<!DOCTYPE html>
<html lang="en">
<head>
<meta charset="utf-8">
<title>Meridale Dental Business Card</title>
<link rel="stylesheet" href="https://fonts.googleapis.com/css2?family=Raleway:wght@300;400;500&display=swap">
<style>
  :root {
    --backdrop: #e9e9e6;
    --lime: #9ee619;
    --lime-light: #b4f23a;
    --lime-deep: #84c90e;
    --ink: #101112;
    --ink-soft: #1e2022;
    --text-dark: #2f3a1c;
    --text-muted: #4a5a2a;
    --brand-text: #e6e8ea;
    --tagline: #8a8f95;
    --rule: rgba(47, 58, 28, 0.45);
  }
  * { box-sizing: border-box; margin: 0; padding: 0; }
  html, body {
    width: 1200px;
    height: 843px;
    overflow: hidden;
    background: var(--backdrop);
    font-family: "Raleway", "Helvetica Neue", Arial, sans-serif;
  }
  .card {
    position: absolute;
    left: 100px;
    top: 136px;
    width: 1000px;
    height: 571px;
    display: flex;
    box-shadow: 0 18px 40px rgba(0, 0, 0, 0.18);
  }
  .card-info {
    position: relative;
    width: 45%;
    background: linear-gradient(160deg, var(--lime-light), var(--lime) 55%, var(--lime-deep));
    color: var(--text-dark);
    text-align: right;
    padding: 0 44px;
  }
  .stripe-texture {
    position: absolute;
    left: 0;
    top: 0;
    width: 100%;
    height: 150px;
    background: linear-gradient(180deg, rgba(255, 255, 255, 0.22), rgba(255, 255, 255, 0));
  }
  .doctor-name {
    position: relative;
    margin-top: 190px;
    font-weight: 300;
    font-size: 34px;
    letter-spacing: 0.5px;
  }
  .doctor-title {
    position: relative;
    margin-top: 6px;
    font-weight: 400;
    font-size: 20px;
    letter-spacing: 1px;
  }
  .divider {
    position: relative;
    margin: 26px 0 22px auto;
    width: 300px;
    height: 1px;
    background: var(--rule);
  }
  .contact {
    position: relative;
    list-style: none;
    font-weight: 400;
    font-size: 17px;
    line-height: 1.65;
    color: var(--text-muted);
  }
  .card-brand {
    position: relative;
    width: 55%;
    background: linear-gradient(150deg, var(--ink-soft), var(--ink) 60%);
    padding: 0 60px;
  }
  .brand-lockup {
    position: absolute;
    left: 60px;
    top: 222px;
    display: flex;
    align-items: center;
    gap: 16px;
  }
  .brand-mark {
    width: 26px;
    height: 26px;
    background: var(--lime);
  }
  .brand-name {
    font-weight: 400;
    font-size: 34px;
    letter-spacing: 0;
    color: var(--brand-text);
  }
  .tagline {
    position: absolute;
    left: 60px;
    top: 310px;
    font-weight: 400;
    font-size: 16px;
    letter-spacing: 0.5px;
    color: var(--tagline);
  }
</style>
</head>
<body>
  <article class="card">
    <section class="card-info">
      <div class="stripe-texture" role="img" aria-label="Fine diagonal stripe texture across the top of the green panel"></div>
      <h1 class="doctor-name">Curtis L. Hobbel</h1>
      <p class="doctor-title">D.D.S.</p>
      <div class="divider"></div>
      <ul class="contact">
        <li>918-555-0147</li>
        <li>20463-C North Fernwick</li>
        <li>Bixby, OK 74031</li>
        <li>www.meridaledentalok.example</li>
      </ul>
    </section>
    <section class="card-brand">
      <div class="brand-lockup">
        <span class="brand-mark"></span>
        <span class="brand-name">Meridale Dental</span>
      </div>
      <p class="tagline">For ALL Your Dental Needs</p>
    </section>
  </article>
</body>
</html>
```